Ridge Fern Electical winter special

I need an ad for a print magazine for my electrical contracting business.
It must have my logo and business name as the main back ground with a banner over the top stating 'winter solar special 10% off'
it must have my licence number in the botomm right corner lic.472915K
It must have my name Derek Whitlam ph 0438215976
Also I would like it to say somewher 'Call now for your free solar assessment'
I would like it on a sharp black bagground like my business card attached and flyer attached
This will be a in a landscape design not potrait
Target Market(s)
Print ad and banner advertising
Industry/Entity Type
Solar Energy
Colors
Designer to choose colors to be used in the design.
Requirements
Must have
- my licence number on bottom right corner
- lic.472915K

```html
<!DOCTYPE html>
<html lang="en">
<head>
<meta charset="utf-8">
<title>Ridge Fern Electical – Winter Solar Special</title>
<link rel="stylesheet" href="https://fonts.googleapis.com/css2?family=Roboto:wght@300;400;500&display=swap">
<style>
  :root {
    --ink-black: #000000;
    --fern-green: #74c281;
    --ocean-blue: #0b5aa6;
    --deep-blue: #0a2d8c;
    --brand-blue: #1c63b8;
    --white: #ffffff;
  }
  * { margin: 0; padding: 0; box-sizing: border-box; }
  html, body {
    width: 1200px; height: 480px; overflow: hidden;
    background: var(--ink-black);
  }
  .ad {
    position: relative; width: 1200px; height: 480px; overflow: hidden;
    background: var(--ink-black);
    font-family: "Roboto", Arial, sans-serif;
    color: var(--white);
  }
  .ad__bands { position: absolute; inset: 0; width: 1200px; height: 480px; }

  .brand {
    position: absolute; left: 60px; top: 118px; width: 340px;
    display: flex; align-items: center; gap: 16px;
  }
  .brand__dot {
    flex: none; width: 40px; height: 40px; border-radius: 50%;
    background: var(--brand-blue);
  }
  .brand__name {
    font-size: 36px; font-weight: 500; letter-spacing: 2px; line-height: 42px;
    color: var(--brand-blue); text-transform: uppercase;
  }

  .offer {
    position: absolute; right: 36px; top: 28px; text-align: right;
  }
  .offer__title {
    font-size: 36px; font-weight: 300; line-height: 34px;
    color: var(--fern-green);
  }
  .offer__amount {
    display: flex; justify-content: flex-end; align-items: flex-start;
    margin-top: 4px;
  }
  .offer__number { font-size: 80px; font-weight: 300; line-height: 76px; letter-spacing: -3px; }
  .offer__suffix {
    display: flex; flex-direction: column; align-items: center;
    font-size: 32px; font-weight: 300; line-height: 28px; margin-left: 2px; margin-top: 4px;
  }

  .services { position: absolute; left: 474px; top: 134px; }
  .services__heading {
    font-size: 38px; font-weight: 300; color: var(--fern-green); margin-bottom: 20px;
  }
  .services__list { list-style: none; }
  .services__item {
    position: relative; padding-left: 13px;
    font-size: 20.5px; font-weight: 300; line-height: 26.5px;
  }
  .services__item::before {
    content: ""; position: absolute; left: 0; top: 8px;
    width: 9px; height: 9px; border-radius: 50%; background: var(--fern-green);
  }

  .call-to-action {
    position: absolute; left: 26px; top: 369px;
    font-size: 21px; font-weight: 300; line-height: 24px; color: var(--fern-green);
  }
  .contact {
    position: absolute; left: 26px; top: 430px;
    display: flex; align-items: center;
    font-size: 24px; font-weight: 300;
  }
  .contact__name { margin-right: 18px; }
  .contact__item { display: flex; align-items: center; gap: 3px; margin-right: 18px; }
  .contact__icon { width: 22px; height: 22px; }
  .licence {
    position: absolute; right: 32px; top: 402px;
    font-size: 19px; font-weight: 300; color: var(--fern-green);
  }
</style>
</head>
<body>
<main class="ad">
  <svg class="ad__bands" viewBox="0 0 1200 480" aria-hidden="true">
    <defs>
      <linearGradient id="band-blue" x1="0" y1="0" x2="1" y2="0">
        <stop offset="0" stop-color="var(--ocean-blue)"/>
        <stop offset="1" stop-color="var(--deep-blue)"/>
      </linearGradient>
      <linearGradient id="corner-blue" x1="0" y1="0" x2="1" y2="1">
        <stop offset="0" stop-color="#0c64ac"/>
        <stop offset="1" stop-color="var(--deep-blue)"/>
      </linearGradient>
    </defs>
    <polygon points="808,0 850,0 1200,300 1200,352" fill="var(--fern-green)"/>
    <polygon points="850,0 1200,0 1200,300" fill="url(#corner-blue)"/>
    <polygon points="0,282 1200,474 1200,480 0,314" fill="var(--fern-green)"/>
    <polygon points="0,314 1200,470 1200,480 0,480" fill="url(#band-blue)"/>
  </svg>

  <div class="brand">
    <span class="brand__dot"></span>
    <span class="brand__name">Ridge Fern<br>Electical</span>
  </div>

  <div class="offer">
    <p class="offer__title">winter solar<br>special</p>
    <div class="offer__amount">
      <span class="offer__number">10</span>
      <span class="offer__suffix"><span>%</span><span>off</span></span>
    </div>
  </div>

  <section class="services">
    <h2 class="services__heading">Specialising in</h2>
    <ul class="services__list">
      <li class="services__item">Solar design and installation</li>
      <li class="services__item">All your domestic and commercial electrical needs</li>
      <li class="services__item">Outstanding customer service</li>
      <li class="services__item">Competitive rates</li>
    </ul>
  </section>

  <p class="call-to-action">Call now for your<br>free solar assessment</p>

  <div class="contact">
    <span class="contact__name">Derek Whitlam</span>
    <span class="contact__item">
      <svg class="contact__icon" viewBox="0 0 24 24" aria-hidden="true">
        <path d="M6.6 3.5l3 3.2-1.8 2.3c1.2 2.5 3.2 4.5 5.7 5.7l2.3-1.8 3.2 3-2.1 3.1C10.4 18.8 5.2 13.6 4.1 5.6z" fill="var(--fern-green)"/>
      </svg>
      0438215976
    </span>
    <span class="contact__item">
      <svg class="contact__icon" viewBox="0 0 24 24" aria-hidden="true">
        <rect x="2" y="6" width="20" height="14" rx="1.5" fill="var(--fern-green)"/>
        <path d="M2.5 7l9.5 7 9.5-7" fill="none" stroke="var(--ocean-blue)" stroke-width="1.6"/>
      </svg>
      info@ridgefernelectrical.com.au
    </span>
  </div>

  <p class="licence">lic.472915K</p>
</main>
</body>
</html>
```